Supplement Rebranding Bottle Design

READ WORD DOCUMENT ATTACHED.
We want to rebrand our current health supplements (see below). We do want it to be modern, vibrant and appealing. Very upscale and elegant as it targets primarily women.
Bottle size: see pictures for bottle size, along with sample bottles that we like; we’re open to any bottle similar to the ones attached.
Current bottles: So ideally, we’d keep the core color on each bottle with a new branding/bottle design. But we're open to your suggestion.

Target Market(s)

mostly women but shouldn't be overly feminine

Requirements
Must have
• see bottle sizes attached

```html
<!DOCTYPE html>
<html lang="en">
<head>
<meta charset="utf-8">
<title>Hepa Lumen – Label</title>
<link href="https://fonts.googleapis.com/css2?family=Lexend:wght@300;400;500;600&display=swap" rel="stylesheet">
<style>
  :root {
    --page-bg: #ffffff;
    --violet-deep: #33007a;
    --violet-mid: #5a12a6;
    --violet-bright: #c43fdc;
    --orchid: #d86bf5;
    --orchid-line: #b95ff0;
    --ink-light: #ffffff;
  }
  * { margin: 0; padding: 0; box-sizing: border-box; }
  html, body {
    width: 797px;
    height: 1200px;
    overflow: hidden;
    background: var(--page-bg);
    font-family: "Lexend", sans-serif;
  }
  .canvas {
    position: relative;
    width: 797px;
    height: 1200px;
  }
  .label {
    position: absolute;
    left: 30px;
    top: 306px;
    width: 737px;
    height: 587px;
    overflow: hidden;
    background:
      radial-gradient(ellipse 70% 45% at 50% 105%, var(--violet-bright) 0%, rgba(196,63,220,0) 100%),
      linear-gradient(180deg, var(--violet-deep) 0%, var(--violet-mid) 55%, #8a26c4 100%);
    color: var(--ink-light);
  }
  .guide-lines {
    position: absolute;
    inset: 0;
    width: 100%;
    height: 100%;
  }
  .organ-illustration {
    position: absolute;
    left: 164px;
    top: 104px;
    width: 213px;
    height: 172px;
    border-radius: 48% 52% 40% 60% / 45% 40% 60% 55%;
    background: radial-gradient(ellipse at 45% 45%, rgba(216,107,245,0.35), rgba(216,107,245,0.08) 70%, rgba(216,107,245,0) 100%);
  }
  .claims {
    position: absolute;
    right: 84px;
    top: 88px;
    width: 300px;
    text-align: right;
  }
  .claims__headline {
    font-weight: 500;
    font-size: 20px;
    line-height: 25px;
    letter-spacing: -0.06em;
    text-transform: uppercase;
  }
  .claims__type {
    position: absolute;
    right: 0;
    top: 70px;
    font-weight: 400;
    font-size: 19.5px;
    letter-spacing: -0.04em;
    white-space: nowrap;
  }
  .claims__count {
    position: absolute;
    right: 0;
    top: 114px;
    font-weight: 400;
    font-size: 18.5px;
    letter-spacing: -0.04em;
  }
  .claims__form {
    position: absolute;
    right: 0;
    top: 138px;
    font-weight: 300;
    font-size: 14.5px;
    letter-spacing: -0.03em;
    white-space: nowrap;
  }
  .product-name {
    position: absolute;
    left: 168px;
    top: 310px;
    font-weight: 600;
    font-size: 106px;
    line-height: 102px;
    letter-spacing: -0.07em;
    color: var(--ink-light);
  }
  .product-name span { display: block; }
</style>
</head>
<body>
  <main class="canvas">
    <section class="label">
      <svg class="guide-lines" viewBox="0 0 737 587" aria-hidden="true">
        <path d="M0 215 H110 C140 215 150 200 164 188" fill="none" stroke="var(--orchid-line)" stroke-width="1.2"/>
        <path d="M377 175 C400 168 420 180 440 192 H653" fill="none" stroke="var(--orchid-line)" stroke-width="1.2"/>
        <line x1="448" y1="152" x2="653" y2="152" stroke="var(--orchid-line)" stroke-width="1"/>
      </svg>
      <div class="organ-illustration" role="img" aria-label="Single-line drawing of a liver in orchid outline"></div>

      <div class="claims">
        <p class="claims__headline">Rejuvenating Cleanse<br>&amp; Detox Formula</p>
        <p class="claims__type">Dietary Supplement</p>
        <p class="claims__count">120</p>
        <p class="claims__form">Vegetable Capsules</p>
      </div>

      <h1 class="product-name"><span>Hepa</span><span>Lumen</span></h1>
    </section>
  </main>
</body>
</html>
```